Website redesign for Root and Renew

We would like to update the design of our current website to a more concise, conversion optimized design.
The goal of our website is to get our message across as concisely as possible plus encourage people to contact us for more information or to book a consultation.
We need a redesign of the home page and 1 internal page - just for design/layout purposes/format purposes.

Target Market(s)

Males 20-45 years old who are concerned about hair loss and who want to regrow their own hair.

Industry/Entity Type

Health And Wellness

Number of Pages Required

2 page

Font styles to use
Sans Serif

Colors
00a990
33a6d7
ffffff
9d9d9d

Requirements
Must have
• We want the home page to be very concise and to the point in getting the message across. We want to get across the following 6 key messages:
• 1. Dr Brambury story – why he created this solution
• 2. Hair loss is caused by a chemical imbalance
• 3. Root and renew conducts genetic and DNA analysis, then rebalances body chemistry, thus reversing the hair loss process and enabling your own hair to regrow naturally
• 4. Money back guaranteed results
• 5. Purely The Core ingredients – no harsh preservatives or chemicals are included
• 6. All ingredients are FDA approved and safe – no side effects
• We also need a strong call to action. We want people to call or email us to find out more information or to schedule a consultation.
• Here is our current website which is not performing as we would hope: http://www.rootandrenewhq.com/
• Here is our press release for further information: https://www.pressflarex.com/news/finally-we-now-have-a-cure-for-male-pattern-baldness-40528316
• I uploaded the logo files, but let me know if anything else is needed and I can add it.

```html
<!DOCTYPE html>
<html lang="en">
<head>
<meta charset="utf-8">
<title>Root and Renew – Home</title>
<link href="https://fonts.googleapis.com/css2?family=Raleway:wght@400;500;600;700&display=swap" rel="stylesheet">
<style>
:root{
  --teal:#00a990;
  --teal-dark:#0a4a3e;
  --blue:#33a6d7;
  --white:#ffffff;
  --grey:#9d9d9d;
  --text:#333333;
  --body:#6b6b6b;
  --dark:#2a2420;
  --red:#e0322f;
}
*{box-sizing:border-box;margin:0;padding:0}
html,body{width:1200px;height:2528px;overflow:hidden;background:var(--white)}
body{position:relative;font-family:'Raleway',sans-serif;color:var(--text)}
.abs{position:absolute}

/* header */
.brand{left:100px;top:18px;width:400px}
.brand-name{font-size:40px;font-weight:500;color:var(--grey);letter-spacing:1px;line-height:44px;display:flex;align-items:center;gap:12px}
.brand-mark{width:34px;height:34px;border-radius:50%;background:var(--teal)}
.brand-by{font-size:20px;color:var(--blue);text-align:right;padding-right:8px;border-top:2px solid #ccc;margin-top:2px;width:390px}
.call{left:740px;top:24px;display:flex;gap:12px;align-items:center}
.call-badge{width:44px;height:44px;border-radius:50%;background:var(--blue)}
.call-label{font-size:15px;color:var(--grey)}
.call-number{font-size:21px;color:var(--grey)}
.btn-book{left:980px;top:28px;width:120px;height:40px;background:var(--blue);color:var(--white);font-size:17px;font-weight:500;display:flex;align-items:center;justify-content:center}

/* nav */
.nav{left:0;top:100px;width:1200px;height:52px;background:var(--teal)}
.nav ul{list-style:none;display:flex;height:52px;padding-left:100px}
.nav li{color:var(--white);font-size:13px;font-weight:600;display:flex;align-items:center;padding:0 20px}
.nav li.active{background:var(--teal-dark);padding:0 38px}
.nav li:nth-child(2){padding-left:24px}

/* hero */
.hero{left:0;top:152px;width:1200px;height:458px;background:linear-gradient(100deg,#8a7666 0%,#c9b09a 35%,#d9c3b0 55%,#9aa3a8 85%,#c4c9cc 100%)}
.hero-curve{left:0;top:500px}
.hero-title{left:100px;top:284px;font-size:34px;font-weight:700;color:var(--white);line-height:54px}
.hero-btn{left:100px;top:414px;width:124px;height:32px;border:2px solid var(--white);border-radius:16px;color:var(--white);font-size:12px;font-weight:600;display:flex;align-items:center;justify-content:center}
.hero-arrow{top:348px}

/* story */
.story-title{left:100px;top:674px;font-size:25px;font-weight:600;color:var(--blue)}
.story-lead{left:100px;top:724px;font-size:14px;font-weight:700;color:var(--text)}
.story-text{left:100px;top:760px;width:510px;font-size:12.5px;line-height:25px;color:var(--body)}
.btn-outline{height:38px;border:2px solid var(--blue);border-radius:20px;color:var(--blue);font-size:12px;font-weight:600;display:flex;align-items:center;justify-content:center}
.story-btn{left:100px;top:900px;width:148px}
.video{left:671px;top:679px;width:428px;height:258px;border:4px solid #e6e6e6;background:#222}
.video-pane{position:absolute;top:0;height:220px;width:50%}
.video-left{left:0;background:linear-gradient(135deg,#6b4c3c,#a9836c)}
.video-right{right:0;background:linear-gradient(135deg,#2b2420,#5c4a3e)}
.video-bar{position:absolute;left:0;bottom:0;width:100%;height:30px;background:#111}
.video-track{position:absolute;left:8px;right:8px;top:4px;height:3px;background:#555}
.video-play{position:absolute;left:190px;top:90px}

/* why */
.why{left:0;top:1006px}
.why-title{left:0;width:1200px;top:1048px;text-align:center;font-size:24px;font-weight:600;color:var(--white)}
.why-circle{top:1088px;width:150px;height:150px;border-radius:50%;background:var(--white);border:3px solid var(--blue);display:flex;justify-content:center;padding-top:30px}
.why-card{top:1203px;width:305px;height:120px;background:var(--white);border:3px solid var(--blue);text-align:center;padding-top:36px}
.why-card h3{font-size:17px;font-weight:600;color:var(--blue)}
.why-card p{font-size:12px;font-weight:700;color:var(--text);margin-top:16px}

/* before after */
.ba-title{left:0;width:1200px;top:1452px;text-align:center;font-size:27px;font-weight:700;color:var(--text)}
.ba-item{top:1525px;width:246px}
.ba-photo{height:140px;background:linear-gradient(90deg,#d9d3cd 0%,#3a2f2a 30%,#e6e1dc 50%,#2d2622 75%,#dcd6d0 100%)}
.ba-text{font-size:12.5px;line-height:26px;color:var(--body);margin-top:22px}
.ba-more{font-size:12px;color:var(--red);text-decoration:underline;margin-top:2px}
.ba-arrow{top:1584px}

/* cta */
.cta{left:0;top:1816px;width:1200px;height:236px;background:linear-gradient(90deg,#2e2723 0%,#4a3a30 45%,#1c1714 100%)}
.cta-text{left:100px;top:1860px;font-size:22px;font-weight:600;color:var(--white);line-height:39px;width:960px}
.cta-btn{left:100px;top:1957px;width:183px;height:42px;border-radius:21px;background:var(--blue);color:var(--white);font-size:13px;font-weight:700;display:flex;align-items:center;justify-content:center}

/* footer */
.foot-h{top:2120px;font-size:18px;font-weight:700;color:var(--text)}
.contact-row{left:100px;display:flex;align-items:flex-start;gap:22px;font-size:13px;line-height:22px;color:var(--body)}
.ring{width:40px;height:40px;border-radius:50%;border:2px solid var(--blue);display:flex;align-items:center;justify-content:center;flex:none}
.foot-brand{left:440px;top:2124px;width:330px}
.foot-brand .brand-name{font-size:30px;line-height:34px}
.foot-brand .brand-by{font-size:17px;width:320px}
.news-h{left:444px;top:2230px;font-size:21px;font-weight:700;color:var(--text)}
.news-text{left:444px;top:2272px;width:380px;font-size:12.5px;line-height:24px;color:var(--body)}
.news-form{left:443px;top:2344px;width:325px;height:39px;display:flex}
.news-input{flex:1;border:1px solid var(--blue);border-radius:6px 0 0 6px;font-size:11px;color:var(--grey);display:flex;align-items:center;padding-left:14px}
.news-send{width:97px;background:var(--blue);color:var(--white);border-radius:0 6px 6px 0;font-size:16px;font-weight:700;display:flex;align-items:center;justify-content:center}
.social{left:972px;display:flex;align-items:center;gap:18px;font-size:13px;color:var(--body)}
.foot-line{left:100px;top:2457px;width:1000px;height:1px;background:#dcdcdc}
.copyright{left:0;width:1200px;top:2480px;text-align:center;font-size:12px;color:var(--body)}
</style>
</head>
<body>

<header>
  <div class="abs brand">
    <div class="brand-name"><span class="brand-mark"></span>Root &amp; Renew</div>
    <div class="brand-by">by Edwin Brambury M.D.</div>
  </div>
  <div class="abs call">
    <span class="call-badge"></span>
    <div><div class="call-label">Call Now :</div><div class="call-number">(310) 555-0142</div></div>
  </div>
  <a class="abs btn-book">BOOK NOW</a>
</header>

<nav class="abs nav">
  <ul>
    <li class="active">HOME</li><li>ABOUT US</li><li>HOW IT WORKS</li><li>SUCCESS STORIES</li><li style="padding:0 34px">BLOG</li><li>FAQS</li><li>SALON PARTNERS</li><li>CONTACT</li>
  </ul>
</nav>

<section>
  <div class="abs hero" role="img" aria-label="Photo of a young man checking his hairline in a mirror"></div>
  <svg class="abs hero-curve" width="1200" height="120" viewBox="0 0 1200 120"><path d="M0 30 Q600 170 1200 30 L1200 120 L0 120Z" fill="#ffffff"/></svg>
  <h1 class="abs hero-title">Root and Renew uses a scientific approach<br>to preventing hair loss and regrowing your hair</h1>
  <a class="abs hero-btn">READ MORE &gt;&gt;</a>
  <svg class="abs hero-arrow" style="left:40px" width="24" height="36" viewBox="0 0 24 36"><path d="M20 3 L5 18 L20 33" stroke="#fff" stroke-width="5" fill="none"/></svg>
  <svg class="abs hero-arrow" style="left:1126px" width="24" height="36" viewBox="0 0 24 36"><path d="M4 3 L19 18 L4 33" stroke="#fff" stroke-width="5" fill="none"/></svg>
</section>

<section>
  <h2 class="abs story-title">Dr Brambury's Story</h2>
  <p class="abs story-lead">Dr Brambury's discovery and development of the Root &amp; Renew™ hair loss solution.</p>
  <p class="abs story-text">Dr. Edwin Brambury is a renowned hair restoration expert and was even a contributor in the development of the Advanced High Density MICROscopic single hair transplant procedure. As a practicing derma-surgeon, he also pioneered the non-surgical rhinoplasty and has a special interest in the field of developing non-surgical solutions to cosmetic problems which have previously been addressed only via surgical means.</p>
  <a class="abs btn-outline story-btn">READ MORE &gt;&gt;</a>
  <div class="abs video">
    <div class="video-pane video-left" role="img" aria-label="Video still of a thinning scalp before treatment"></div>
    <div class="video-pane video-right" role="img" aria-label="Video still of the same scalp with regrown hair"></div>
    <svg class="video-play" width="36" height="36" viewBox="0 0 36 36"><circle cx="18" cy="18" r="17" fill="#fff"/><path d="M14 10 L26 18 L14 26Z" fill="#222"/></svg>
    <div class="video-bar"><div class="video-track"></div></div>
  </div>
</section>

<section>
  <svg class="abs why" width="1200" height="389" viewBox="0 0 1200 389"><path d="M0 30 Q600 -30 1200 30 L1200 340 Q600 420 0 340Z" fill="#00a990"/></svg>
  <h2 class="abs why-title">WHY CHOOSE US</h2>

  <div class="abs why-circle" style="left:177px">
    <svg width="80" height="56" viewBox="0 0 80 56" fill="none" stroke="#33a6d7" stroke-width="3"><path d="M6 20 H62 L52 10 M74 36 H18 L28 46"/><circle cx="40" cy="28" r="12"/><path d="M44 22 H38 a3 3 0 0 0 0 6 h4 a3 3 0 0 1 0 6 H36 M40 19 V37"/></svg>
  </div>
  <div class="abs why-circle" style="left:521px">
    <svg width="60" height="56" viewBox="0 0 60 56" fill="none" stroke="#33a6d7" stroke-width="3"><rect x="4" y="12" width="52" height="40" rx="3"/><path d="M22 12 V5 H38 V12 M30 22 V42 M20 32 H40"/></svg>
  </div>
  <div class="abs why-circle" style="left:868px">
    <svg width="60" height="56" viewBox="0 0 60 56" fill="none" stroke="#33a6d7" stroke-width="3"><path d="M8 44 L22 54 L52 8"/></svg>
  </div>

  <div class="abs why-card" style="left:101px"><h3>Money back guaranteed results</h3><p>Lorem ipsum dolor sit amet</p></div>
  <div class="abs why-card" style="left:448px"><h3>Preservatives</h3><p>Lorem ipsum dolor sit amet</p></div>
  <div class="abs why-card" style="left:794px"><h3>FDA approved and safe</h3><p>Lorem ipsum dolor sit amet</p></div>
</section>

<section>
  <h2 class="abs ba-title">Before and After</h2>
  <svg class="abs ba-arrow" style="left:50px" width="20" height="30" viewBox="0 0 20 30"><path d="M16 3 L4 15 L16 27" stroke="#666" stroke-width="3" fill="none"/></svg>
  <svg class="abs ba-arrow" style="left:1132px" width="20" height="30" viewBox="0 0 20 30"><path d="M4 3 L16 15 L4 27" stroke="#666" stroke-width="3" fill="none"/></svg>

  <div class="abs ba-item" style="left:101px"><div class="ba-photo" role="img" aria-label="Before and after photos of a man's crown"></div><p class="ba-text">Quisque aliquet mauris luctus erat ornare vehicula.</p><p class="ba-more">Read More..</p></div>
  <div class="abs ba-item" style="left:354px"><div class="ba-photo" role="img" aria-label="Before and after photos of a hairline after four months"></div><p class="ba-text">Quisque aliquet mauris luctus erat ornare vehicula.</p><p class="ba-more">Read More..</p></div>
  <div class="abs ba-item" style="left:610px"><div class="ba-photo" role="img" aria-label="Before and after photos of a scalp after three months"></div><p class="ba-text">Quisque aliquet mauris luctus erat ornare vehicula.</p><p class="ba-more">Read More..</p></div>
  <div class="abs ba-item" style="left:863px"><div class="ba-photo" role="img" aria-label="Before and after photos of a crown after four months"></div><p class="ba-text">Quisque aliquet mauris luctus erat ornare vehicula.</p><p class="ba-more">Read More..</p></div>
</section>

<section>
  <div class="abs cta" role="img" aria-label="Close-up photo of a comb running through dark hair"></div>
  <p class="abs cta-text">Root and renew conducts genetic and DNA analysis, then rebalancesbody chemistry, thus reversing the hair loss process and enabling your own hair to regrow naturally</p>
  <a class="abs cta-btn">GET STARTED NOW</a>
</section>

<footer>
  <h4 class="abs foot-h" style="left:100px">GET IN TOUCH</h4>
  <div class="abs contact-row" style="top:2172px">
    <span class="ring"><svg width="18" height="18" viewBox="0 0 24 24" fill="#33a6d7"><path d="M6.6 10.8a15 15 0 0 0 6.6 6.6l2.2-2.2a1 1 0 0 1 1-.25 11 11 0 0 0 3.6.6 1 1 0 0 1 1 1V20a1 1 0 0 1-1 1A17 17 0 0 1 3 4a1 1 0 0 1 1-1h3.5a1 1 0 0 1 1 1 11 11 0 0 0 .6 3.6 1 1 0 0 1-.25 1z"/></svg></span>
    <span style="padding-top:9px">(310) 555-0142</span>
  </div>
  <div class="abs contact-row" style="top:2226px">
    <span class="ring"><svg width="16" height="20" viewBox="0 0 16 20" fill="#33a6d7"><path d="M8 0a7 7 0 0 0-7 7c0 5 7 13 7 13s7-8 7-13a7 7 0 0 0-7-7zm0 10a3 3 0 1 1 0-6 3 3 0 0 1 0 6z"/></svg></span>
    <span>Root and Renew Hair, LLC<br>2871 Larkspur Ave, Suite 300<br>Glenmere CA 90417</span>
  </div>
  <div class="abs contact-row" style="top:2310px">
    <span class="ring"><svg width="20" height="20" viewBox="0 0 20 20" fill="none" stroke="#33a6d7" stroke-width="1.6"><circle cx="10" cy="10" r="8.5"/><ellipse cx="10" cy="10" rx="3.8" ry="8.5"/><path d="M1.5 10h17"/></svg></span>
    <span style="padding-top:9px">www.rootandrenewhq.com</span>
  </div>

  <div class="abs foot-brand">
    <div class="brand-name"><span class="brand-mark" style="width:28px;height:28px"></span>Root &amp; Renew</div>
    <div class="brand-by">by Edwin Brambury M.D.</div>
  </div>
  <h4 class="abs news-h">NewsLetter</h4>
  <p class="abs news-text">Lorem ipsum dolor sit amet, consectetur adipiscing elit. Vivamus lacus orci, tempor ac felis et, gravida scelerisque tortor.</p>
  <div class="abs news-form"><span class="news-input">Enter Your Mail ID..</span><span class="news-send">Send</span></div>

  <h4 class="abs foot-h" style="left:968px">SOCIAL MEDIA</h4>
  <div class="abs social" style="top:2172px"><span class="ring"></span>Friendbook</div>
  <div class="abs social" style="top:2227px"><span class="ring"></span>Chirper</div>
  <div class="abs social" style="top:2280px"><span class="ring"></span>Linkwork</div>
  <div class="abs social" style="top:2332px"><span class="ring"></span>Circleplus</div>
  <div class="abs social" style="top:2384px"><span class="ring"></span>Vidtube</div>

  <div class="abs foot-line"></div>
  <p class="abs copyright">Copyright ©2017 RootandRenew.All rights reserved.</p>
</footer>

</body>
</html>
```